KL Taxidermy

I need business Cards with my logo and a background photo of one of my taxidermy mounts.
I would like a black back drop behind it all and what ever looks best for my contact information (red or white?)
Garrick Pembley
592-718-4409
kltaxidermy482@mailnook.example
Chatterloom page

```html
<!DOCTYPE html>
<html lang="en">
<head>
<meta charset="utf-8">
<title>KL Taxidermy – Business Card</title>
<link rel="stylesheet" href="https://fonts.googleapis.com/css2?family=Exo+2:wght@400;500;600&display=swap">
<style>
  :root {
    --backdrop: #8c8c8c;
    --card-black: #1e1e1e;
    --silver: #d9d9d9;
    --silver-dim: #b8b8b8;
    --fleece: #ecebe6;
    --horn: #8a5a30;
  }
  * { margin: 0; padding: 0; box-sizing: border-box; }
  html, body { width: 1200px; height: 884px; overflow: hidden; }
  body {
    background: var(--backdrop);
    font-family: "Exo 2", sans-serif;
    position: relative;
  }
  .card {
    position: absolute;
    left: 80px; top: 145px;
    width: 1040px; height: 594px;
    background: var(--card-black);
    overflow: hidden;
  }
  .brand {
    position: absolute;
    left: 96px; top: 70px;
    display: flex; align-items: center; gap: 14px;
    color: var(--silver);
    font-size: 34px; font-weight: 600;
    letter-spacing: 1px;
    text-transform: uppercase;
    z-index: 2;
  }
  .brand-mark {
    width: 30px; height: 30px;
    background: var(--silver);
  }
  .holder-name {
    position: absolute;
    left: 92px; top: 258px;
    color: var(--silver);
    font-size: 42px; font-weight: 500;
    letter-spacing: 1px;
    text-transform: uppercase;
    z-index: 2;
  }
  .contact-list {
    position: absolute;
    left: 92px; top: 340px;
    list-style: none;
    color: var(--silver-dim);
    font-size: 25px;
    z-index: 2;
  }
  .contact-list li {
    display: flex; align-items: center; gap: 12px;
    height: 40px;
    white-space: nowrap;
  }
  .contact-icon { width: 20px; height: 20px; flex: none; }
  .social-square { width: 18px; height: 18px; background: var(--silver-dim); flex: none; margin: 0 1px; }
  .mount-photo {
    position: absolute;
    left: 640px; top: 50px;
    width: 350px; height: 500px;
    background: radial-gradient(ellipse at 55% 58%, var(--fleece) 0%, #d8d6cf 40%, var(--horn) 62%, var(--card-black) 72%);
    z-index: 1;
  }
</style>
</head>
<body>
  <section class="card">
    <div class="brand"><span class="brand-mark"></span><span>KL Taxidermy</span></div>
    <h1 class="holder-name">Garrick Pembley</h1>
    <ul class="contact-list">
      <li>
        <svg class="contact-icon" viewBox="0 0 24 24" fill="#b8b8b8"><path d="M6.6 10.8a15 15 0 0 0 6.6 6.6l2.2-2.2a1 1 0 0 1 1-.25 11.4 11.4 0 0 0 3.6.6 1 1 0 0 1 1 1V20a1 1 0 0 1-1 1A17 17 0 0 1 3 4a1 1 0 0 1 1-1h3.5a1 1 0 0 1 1 1c0 1.25.2 2.45.6 3.6a1 1 0 0 1-.25 1z"/></svg>
        <span>592-718-4409</span>
      </li>
      <li>
        <svg class="contact-icon" viewBox="0 0 24 24" fill="none" stroke="#b8b8b8" stroke-width="2"><rect x="2" y="5" width="20" height="14"/><path d="M2 5l10 8 10-8"/></svg>
        <span>kltaxidermy482@mailnook.example</span>
      </li>
      <li>
        <span class="social-square"></span>
        <span>/KLTaxiDermy</span>
      </li>
    </ul>
    <div class="mount-photo" role="img" aria-label="Photo of a white Dall sheep ram shoulder mount with curled brown horns, facing left"></div>
  </section>
</body>
</html>
```